Business Card for Quillmark Ledger - A cannabis publication for executives.

I'd like some business cards for Quillmark Ledger. The logo is done (great job!) and I need a card design I will use with PRINTLY. I made it a short project to allow time for printing before an event. These will be standard sized cards (final artwork size 3.66" x 2.16" at 300dpi) with a final card size of 3.5" x 2.0". (See PRINTLY.com if you need more info.) I might try rounded corners but am not sure yet. I think the design will work okay with rounded.

Quillmark Ledger will be a bi-weekly publication for the cannabis industry. It is targeted to investors and industry executives, not consumers or pot smokers. So our market is more B2B. However I am open to creativity and making the card something people remark on.

My contact for card:

Dana Merrow
Founder/CEO
dana@quillmarkledger.example

2740 Harlow Avenue
Boston MA 02135
(617)555-0194

Target Market(s)

Executives, Industry people and investors in the Cannabis sector.

Contact Information for Business Card

PRINTLY does do double sided and the second side can be the same or different images. Only one side is required but use of the second side would be a bonus.

Font styles to use
Serif
Sans Serif
Decorative

Colors

Designer to choose colors to be used in the design.

Requirements
Must have
• Logo, contact info
Nice to have
• Style and design to make the card stand out in a crowd.

```html
<!DOCTYPE html>
<html lang="en">
<head>
<meta charset="utf-8">
<title>Quillmark Ledger — Business Card</title>
<link rel="stylesheet" href="https://fonts.googleapis.com/css2?family=Exo+2:wght@700&family=Open+Sans:wght@400;600&display=swap">
<style>
  :root {
    --brand-blue: #1b73bf;
    --brand-green: #7cb82f;
    --ink-grey: #555a60;
    --card-white: #ffffff;
    --backdrop: #e9eaec;
  }
  * { margin: 0; padding: 0; box-sizing: border-box; }
  html, body {
    width: 1200px; height: 1000px; overflow: hidden;
    background: var(--backdrop);
    font-family: "Open Sans", Arial, sans-serif;
  }
  .card {
    position: absolute; left: 250px;
    width: 700px; height: 400px;
    border-radius: 22px;
    box-shadow: 0 6px 18px rgba(0,0,0,.18);
  }
  .card--front { top: 55px; background: var(--brand-blue); display: flex; align-items: center; justify-content: center; }
  .card--back { top: 525px; background: var(--card-white); }

  .wordmark { display: flex; align-items: center; gap: 14px; font-weight: 600; font-family: "Open Sans", Arial, sans-serif; }
  .wordmark__dot { width: 40px; height: 40px; border-radius: 50%; }
  .card--front .wordmark { font-size: 44px; color: var(--card-white); }
  .card--front .wordmark__dot { background: var(--brand-green); width: 56px; height: 56px; }
  .card--back .wordmark { position: absolute; right: 40px; top: 50px; font-size: 34px; color: var(--brand-blue); }
  .card--back .wordmark__dot { background: var(--brand-green); }

  .holder { position: absolute; left: 40px; top: 118px; }
  .holder__name { font-family: "Exo 2", Arial, sans-serif; font-weight: 700; font-size: 31px; color: var(--brand-blue); line-height: 1.1; }
  .holder__role { font-size: 20px; color: var(--ink-grey); line-height: 1.3; }
  .rule { position: absolute; left: 36px; right: 36px; top: 188px; height: 2px; background: var(--brand-blue); }

  .contacts { position: absolute; left: 40px; top: 218px; list-style: none; }
  .contacts li { display: flex; align-items: center; gap: 12px; font-size: 18px; color: var(--ink-grey); line-height: 27px; }
  .contacts svg { width: 16px; height: 16px; fill: var(--brand-blue); flex: none; }
  .contacts .accent { color: var(--brand-blue); }

  .address { position: absolute; right: 40px; top: 300px; text-align: right; font-size: 19px; color: var(--ink-grey); line-height: 27px; }
  .address__pin { position: absolute; right: -2px; top: -18px; width: 16px; height: 14px; }
</style>
</head>
<body>
  <section class="card card--front" aria-label="Card front">
    <div class="wordmark"><span class="wordmark__dot"></span>Quillmark Ledger</div>
  </section>

  <section class="card card--back" aria-label="Card back">
    <div class="wordmark"><span class="wordmark__dot"></span>Quillmark Ledger</div>

    <div class="holder">
      <p class="holder__name">Dana Merrow</p>
      <p class="holder__role">Founder/CEO</p>
    </div>
    <div class="rule"></div>

    <ul class="contacts">
      <li>
        <svg viewBox="0 0 16 16" aria-hidden="true"><path d="M3.5 1l2.5 3-1.5 2c1 2 2.5 3.5 4.5 4.5l2-1.5 3 2.5-1.5 3C7 14 2 9 1 2.5z"/></svg>
        (617)555-0194
      </li>
      <li>
        <svg viewBox="0 0 16 16" aria-hidden="true"><path d="M1 3h14v10H1z" fill="none" stroke="#1b73bf" stroke-width="1.6"/><path d="M1 3l7 6 7-6" fill="none" stroke="#1b73bf" stroke-width="1.6"/></svg>
        dana@quillmarkledger.example
      </li>
      <li>
        <svg viewBox="0 0 16 16" aria-hidden="true"><circle cx="9.5" cy="6.5" r="4.5" fill="none" stroke="#1b73bf" stroke-width="2"/><path d="M6 10l-4.5 4.5" stroke="#1b73bf" stroke-width="2.4"/></svg>
        <span>www.<span class="accent">quillmarkledger</span>.example</span>
      </li>
    </ul>

    <address class="address" style="font-style:normal">
      <svg class="address__pin" viewBox="0 0 16 14" aria-hidden="true"><path d="M1 12L15 1 10 13 7 8z" fill="none" stroke="#7cb82f" stroke-width="1.4"/></svg>
      2740 Harlow Avenue<br>Boston MA 02135
    </address>
  </section>
</body>
</html>
```